Verodex business card

Business card for sustainable investment company called "Verodex". Verodex is an exchange platform selling carbon credits between buyers and sellers. Carbon Credits are an environmental commodity for reducing global carbon emissions.

the card should obviously have our logo and the theme should be sustainability/environment mixed with a trading platform.

Contact Information for Business Card

Logo, Name, Title, Phone, Email

Colors
0054AA
0677BA
7BADD7
CADEEF
E8F1F8
0094D4
00A9DD
6FCCEA
C7EBF8
E9F6FB
00AB8E
00BBA5
67D7C9
C6EFE9
E9F9F6
59FF00
82FF00
B8FF75
E3FFCB
F4FFEA

```html
<!DOCTYPE html>
<html lang="en">
<head>
<meta charset="UTF-8">
<title>Verodex business card</title>
<link href="https://fonts.googleapis.com/css2?family=Quicksand:wght@500;600;700&display=swap" rel="stylesheet">
<style>
  :root {
    --backdrop: #e9edf2;
    --card-navy: #12295a;
    --card-navy-deep: #0f2350;
    --card-navy-light: #16306a;
    --accent-blue: #4a9fd8;
    --accent-cyan: #6fcCea;
    --ink-white: #ffffff;
    --shadow: rgba(10, 25, 55, 0.28);
  }
  * { box-sizing: border-box; margin: 0; padding: 0; }
  html, body {
    width: 1200px;
    height: 900px;
    overflow: hidden;
    background: var(--backdrop);
    font-family: "Quicksand", sans-serif;
  }
  .sheet {
    width: 1200px;
    height: 900px;
    display: flex;
    flex-direction: column;
    align-items: center;
    justify-content: center;
    gap: 60px;
  }
  .card {
    position: relative;
    width: 630px;
    height: 360px;
    border-radius: 48px 0 48px 0;
    background: linear-gradient(135deg, var(--card-navy-deep) 0%, var(--card-navy) 50%, var(--card-navy-light) 100%);
    box-shadow: 0 18px 36px var(--shadow);
    overflow: hidden;
    color: var(--ink-white);
  }
  .brand {
    position: absolute;
    left: 50%;
    top: 50%;
    transform: translate(-50%, -50%);
    display: flex;
    align-items: center;
    gap: 22px;
  }
  .brand-mark {
    width: 46px;
    height: 46px;
    border-radius: 50%;
    background: var(--accent-blue);
  }
  .brand-name {
    font-weight: 700;
    font-size: 58px;
    letter-spacing: 3px;
    text-transform: uppercase;
    color: var(--ink-white);
  }
  .holder {
    position: absolute;
    left: 44px;
    top: 40px;
    line-height: 1.2;
  }
  .holder-name {
    font-weight: 500;
    font-size: 21px;
    letter-spacing: 1px;
    text-transform: uppercase;
    color: var(--accent-blue);
  }
  .holder-title {
    font-weight: 600;
    font-size: 19px;
    color: var(--ink-white);
  }
  .contact {
    position: absolute;
    right: 40px;
    bottom: 40px;
    list-style: none;
    text-align: right;
    font-weight: 600;
    font-size: 19px;
    line-height: 1.5;
  }
  .contact li {
    display: flex;
    align-items: center;
    justify-content: flex-end;
    gap: 10px;
  }
  .contact svg {
    width: 18px;
    height: 18px;
    fill: var(--accent-cyan);
  }
</style>
</head>
<body>
  <main class="sheet">
    <section class="card card-front" aria-label="Card front">
      <div class="brand">
        <span class="brand-mark"></span>
        <span class="brand-name">Verodex</span>
      </div>
    </section>

    <section class="card card-back" aria-label="Card back">
      <div class="holder">
        <p class="holder-name">Daniel Moreau</p>
        <p class="holder-title">Director</p>
      </div>
      <div class="brand">
        <span class="brand-mark"></span>
        <span class="brand-name">Verodex</span>
      </div>
      <ul class="contact">
        <li>300-418-2763
          <svg viewBox="0 0 24 24" aria-hidden="true"><path d="M6.6 10.8a15.1 15.1 0 0 0 6.6 6.6l2.2-2.2c.3-.3.7-.4 1-.2 1.1.4 2.3.6 3.6.6.6 0 1 .4 1 1V20c0 .6-.4 1-1 1A17 17 0 0 1 3 4c0-.6.4-1 1-1h3.5c.6 0 1 .4 1 1 0 1.3.2 2.5.6 3.6.1.3 0 .7-.2 1z"/></svg>
        </li>
        <li>info@verodex.com
          <svg viewBox="0 0 24 24" aria-hidden="true"><path d="M3 5h18a1 1 0 0 1 1 1v12a1 1 0 0 1-1 1H3a1 1 0 0 1-1-1V6a1 1 0 0 1 1-1zm9 7.2L4 7.5V8l8 5 8-5v-.5z"/></svg>
        </li>
      </ul>
    </section>
  </main>
</body>
</html>
```